Webdesign für Gebäudereinigung
Zielgruppe
Seit 2005 ist LUM Dienstleistungen der Partner für Gebäudereinigung in Berlin. Wir haben Firmenkunden sowie privat Kunden und kümmern uns um sämtliche Reinigungen. Wie Glasreinigung, Büro- und Unterhaltungsreinigung, Bau- und Baufeinreinigung, Aufgangsreinigung & Grundreinigung…
Aufgabenstellung
Unsere neue Webseite sollte modern - Zeitlos - freundlich sein … Farben am Logo orientieren, das übernehmen wir weiterhin….

```html
<!DOCTYPE html>
<html lang="de">
<head>
<meta charset="utf-8">
<title>LUM Dienstleistungen – Gebäudereinigung in Berlin</title>
<link href="https://fonts.googleapis.com/css2?family=Heebo:wght@400;500;700&display=swap" rel="stylesheet">
<style>
  :root{
    --blue:#2f4f88;
    --orange:#ee6a2f;
    --peach:#fde8de;
    --peach-strong:#fbd3c1;
    --text:#333;
    --grey-bg:#f3f3f5;
    --line:#cfd3da;
  }
  *{box-sizing:border-box;margin:0;padding:0}
  html,body{width:1200px;height:2577px;overflow:hidden}
  body{position:relative;background:#fff;font-family:"Heebo",sans-serif;color:var(--text)}
  .abs{position:absolute}
  a{text-decoration:none;color:inherit}

  .brand{left:61px;top:60px;display:flex;align-items:center;gap:12px}
  .brand-mark{width:40px;height:40px;background:var(--blue)}
  .brand-name{font-size:24px;font-weight:500;color:var(--blue)}

  .phone-top{left:723px;top:14px;width:410px;height:39px;background:var(--peach);color:var(--orange);
    font-size:17px;display:flex;align-items:center;justify-content:center;gap:6px}
  .phone-top strong{font-weight:700}

  .nav{right:67px;top:124px;display:flex;gap:44px;font-size:22px;font-weight:500;color:var(--blue)}
  .nav a{padding:0 8px 12px}
  .nav .active{color:var(--orange);border-bottom:2px solid var(--orange)}
  .header-line{left:0;top:164px;width:1200px;height:1px;background:var(--line)}

  .hero{left:0;top:165px;width:1200px;height:313px;
    background:linear-gradient(180deg,#eef2f9 0%,#f7eeea 55%,#f7cdb8 100%)}
  .hero h1{position:absolute;left:63px;top:46px;font-size:36px;line-height:48px;font-weight:700;color:var(--blue)}
  .hero h1 span{display:block;font-weight:400}
  .hero p{position:absolute;left:66px;top:162px;font-size:21px;line-height:35px;color:var(--blue);width:620px}
  .hero p em{font-style:normal;color:var(--orange)}

  .facts{left:110px;top:546px;width:820px}
  .fact{display:flex;gap:26px;font-size:16.5px;line-height:28px;margin-bottom:47px}
  .fact svg{flex:none;width:28px;height:28px;margin-top:2px}

  .values-title{left:61px;top:780px;font-size:29px;line-height:40px;font-weight:400;color:#3a3a3a}

  .photo{width:181px;height:181px;box-shadow:7px 7px 0 var(--peach-strong)}
  .photo-1{left:62px;top:897px;background:linear-gradient(135deg,#8a9a7a,#3b4a32 60%,#6a8a3a)}
  .photo-2{left:447px;top:897px;background:linear-gradient(135deg,#6a4a30,#d8c6b0 50%,#b98d5a)}
  .photo-3{left:839px;top:897px;background:linear-gradient(135deg,#5a8a8a,#9ac07a 55%,#3a6a6a)}

  .value{width:300px;top:1128px}
  .value h2{font-size:29px;font-weight:400;color:var(--orange);line-height:36px;margin-bottom:20px}
  .value p{font-size:16.7px;line-height:28px;margin-bottom:14px}
  .mark{background:var(--peach)}
  .v1{left:62px}.v2{left:446px}.v3{left:837px}

  .cta{left:29px;top:1914px;width:1143px;height:98px;background:var(--peach);
    color:var(--orange);font-size:22px;font-weight:700}
  .cta .label{position:absolute;left:35px;top:34px}
  .cta .num{position:absolute;left:416px;top:34px;display:flex;align-items:center;gap:16px}

  .footer{left:0;top:2069px;width:1200px;height:508px;background:var(--grey-bg)}
  .footer .members-title{position:absolute;left:59px;top:26px;font-size:17px}
  .badge{position:absolute;top:70px;height:52px;background:#dfe3ea;border-radius:4px}
  .b1{left:59px;width:154px}.b2{left:275px;width:252px}.b3{left:571px;width:205px}
  .footer-nav{position:absolute;left:59px;top:222px;display:flex;flex-direction:column;gap:18px;font-size:17px}
  .footer-line{position:absolute;left:59px;top:441px;width:1094px;height:1px;background:#9aa0a8}
  .copy{position:absolute;left:59px;top:462px;font-size:17px}
</style>
</head>
<body>

<header>
  <div class="abs brand"><span class="brand-mark"></span><span class="brand-name">LUM Dienstleistungen</span></div>
  <div class="abs phone-top">Ihre Telefonkontakt für Berlin: <strong>030 555 019 24</strong></div>
  <nav class="abs nav">
    <a class="active" href="#">Start</a>
    <a href="#">Leistungen</a>
    <a href="#">Kontakt</a>
  </nav>
  <div class="abs header-line"></div>
</header>

<section class="abs hero" role="img" aria-label="Helle Skyline von Berlin mit Fernsehturm im Hintergrund">
  <h1>L.U.M. Gebäudereinigung in Berlin,<span>Ihre kompetenter Partner für die Objektreinigung.</span></h1>
  <p>Was uns auszeichnet sind <em>Flexibilität</em>, <em>Zuverlässigkeit</em> und <em>Gründlichkeit</em>.</p>
</section>

<section class="abs facts">
  <div class="fact">
    <svg viewBox="0 0 28 28" fill="none" stroke="var(--orange)" stroke-width="2.2" stroke-linejoin="round"><path d="M4 13 14 4l10 9v11H4z"/><path d="M11 24v-7h6v7"/></svg>
    <p>L.U.M. Gebäudereinigung in Berlin existiert bereits seit 2005 und ist Mitglied der Industrie- und Handelskammer (IHK).</p>
  </div>
  <div class="fact">
    <svg viewBox="0 0 28 28" fill="none" stroke="var(--orange)" stroke-width="2.2" stroke-linecap="round"><circle cx="8" cy="7" r="3.5"/><circle cx="20" cy="7" r="3.5"/><path d="M3 24v-5a5 5 0 0 1 8-4M25 24v-5a5 5 0 0 0-8-4"/></svg>
    <p>Unser Team umfasst derzeit rund 20 Mitarbeiterinnen und Mitarbeiter, die sich allesamt durch fachliches Know-how und eine hohe Motivation auszeichnen.</p>
  </div>
</section>

<h2 class="abs values-title">LUM Dienstleistungen Berlin ist an langfristigen<br>Partnerschaften interessiert und steht für folgende Werte:</h2>

<div class="abs photo photo-1" role="img" aria-label="Reinigungskraft putzt ein Fenster"></div>
<div class="abs photo photo-2" role="img" aria-label="Sauberes, modernes Badezimmer"></div>
<div class="abs photo photo-3" role="img" aria-label="Glasfassade mit grünen Bäumen"></div>

<article class="abs value v1">
  <h2>Flexibel &amp; pünktlich</h2>
  <p>Flexibilität bedeutet im Bereich der Gebäude- und Aufgangsreinigung, dass wir problemlos <span class="mark">auch kurzfristige Aufträge</span> übernehmen. Rufen Sie uns an und wir sind meist in kurzer Zeit mit einem Team vor Ort.</p>
  <p>Gerne übernehmen wir auch die <span class="mark">Urlaubsvertretung</span> für eine fest angestellte Fachkraft und arbeiten auf Wunsch auch für Subunternehmen.</p>
  <p>Flexibilität bedeutet jedoch auch, dass wir gleichermaßen große wie kleine Objekte betreuen. Unabhängig davon, ob Sie einen Partner für ein einzelnes Mehrfamilienhaus oder einen großen Bürokomplex in Berlin suchen: wir unterbreiten Ihnen gerne ein faires Angebot.</p>
</article>

<article class="abs value v2">
  <h2>Kundig &amp; zuverlässig</h2>
  <p>Einer der wichtigsten Punkte unserer Arbeit ist die Zuverlässigkeit. Unabhängig davon, ob Sie mit uns in der <span class="mark">Aufgangsreinigung, Büro-</span> und <span class="mark">Unterhaltsreinigung</span> oder im Bereich <span class="mark">Bau- und Baufeinreinigung</span> zusammen arbeiten.</p>
  <p>Sie können Sie sich auf eine fristgerechte Ausführung aller gewünschten Tätigkeiten verlassen. Anders ausgedrückt: <span class="mark">wir halten Wort</span>, sowohl, was den Umfang unserer Arbeit als auch den Zeitpunkt der Ausführung angeht.</p>
  <p>Möglich wird diese Verlässlichkeit aufgrund unserer langjährigen Erfahrung und unserer flexiblen Teamplanung, die uns immer auch spontane Einsätze in Berlin und Umgebung ermöglicht.</p>
</article>

<article class="abs value v3">
  <h2>Gründlich &amp; sauber</h2>
  <p>Wenn es um die Reinigung von <span class="mark">Wohn- oder Büroflächen, Schwimmbädern, Kitas oder Schulen</span> in Berlin geht, ist Gründlichkeit das A und O. LUM Dienstleistungen führt die Aufträge einerseits schnell, vor allem aber gewissenhaft und mit penibler Sauberkeit aus.</p>
  <p>Hygiene ist ein integraler Bestandteil unserer Arbeitsweise und zeigt sich auch durch die Verwendung hochwertiger Reinigungsmaterialien und <span class="mark">umweltschonender Reinigungsmittel.</span></p>
  <p>Wir wissen, dass die Sauberkeit eines Gebäudes gleichzeitig als „Visitenkarte“ der Bewohner oder des dort ansässigen Unternehmens fungiert und tragen dem in verantwortungsvoller Weise Rechnung. Verlassen Sie sich auf uns.</p>
</article>

<section class="abs cta">
  <span class="label">Wir sind gerne für sie da.</span>
  <span class="num">
    <svg width="28" height="28" viewBox="0 0 28 28" fill="none" stroke="var(--orange)" stroke-width="2" stroke-linejoin="round"><path d="M6 3l4 1 2 6-3 2a14 14 0 0 0 7 7l2-3 6 2 1 4c-1 2-3 3-5 3C11 25 3 17 3 8c0-2 1-4 3-5z"/><path d="M17 4a8 8 0 0 1 7 7M16 8a4 4 0 0 1 4 4" stroke-linecap="round"/></svg>
    030 555 019 24
  </span>
</section>

<footer class="abs footer">
  <p class="members-title">Wir sind Mitglied der:</p>
  <div class="badge b1" role="img" aria-label="Mitgliedsabzeichen Kammer"></div>
  <div class="badge b2" role="img" aria-label="Mitgliedsabzeichen Handwerkskammer"></div>
  <div class="badge b3" role="img" aria-label="Mitgliedsabzeichen Verband"></div>
  <nav class="footer-nav">
    <a href="#">Start</a>
    <a href="#">Leistungen</a>
    <a href="#">Kontakt</a>
    <a href="#">Impressum</a>
    <a href="#">Datenschutz</a>
  </nav>
  <div class="footer-line"></div>
  <p class="copy">© 2022 LUM Gebäudereinigung</p>
</footer>

</body>
</html>
```